LOGO and Business Card Design Project

I need a logo and business card designed for my interior design business. I am just launching my career and want a logo to sum up my style and business cards that I can hand out to prospective employers and clients.
The logo is the most important aspect. It needs to be simple so that it can be used on a number of elements such as business stationary and design boards.
Zentrix top logos of 2012 to see how a simple logo can be really effective at conveying a business identity.
My logo and business card need to quickly express my style.
In a nutshell my style is classic with an edge. If I were in the fashion world my look would be aspiring to be Benedict Oakhurst - velvet storm is a big inspiration.
The name is Tova Interiors. Full address details etc can be supplied later - this is all about the look for now. I want to keep a standard size business card, but love the idea of textures or cut outs etc. This card and logo need to help me stand out from the crowd.

```html
<!DOCTYPE html>
<html lang="en">
<head>
<meta charset="utf-8">
<title>Tova Interiors – Business Card</title>
<link href="https://fonts.googleapis.com/css2?family=Cutive+Mono&family=Open+Sans:wght@400;600&display=swap" rel="stylesheet">
<style>
  :root {
    --backdrop: #35353a;
    --velvet: #38374f;
    --velvet-deep: #2b2a3e;
    --damask-olive: #5d5842;
    --damask-blue: #2e3556;
    --trim-tan: #a89670;
    --parchment: #e2d9c6;
    --parchment-shade: #cbbfa6;
    --frame-stone: #8c8170;
    --frame-dark: #5e5446;
    --ink: #3a3127;
  }
  * { box-sizing: border-box; margin: 0; padding: 0; }
  html, body { width: 1200px; height: 900px; overflow: hidden; }
  body {
    background: var(--backdrop);
    font-family: "Open Sans", sans-serif;
    position: relative;
  }
  .card {
    position: absolute;
    left: 285px;
    width: 630px;
    height: 360px;
    overflow: hidden;
    background: linear-gradient(160deg, var(--velvet), var(--velvet-deep));
    box-shadow: 0 14px 30px rgba(0,0,0,0.45);
  }
  .card--front { top: 50px; }
  .card--back { top: 490px; }

  .damask {
    position: absolute;
    background: radial-gradient(circle at 30% 40%, var(--damask-olive), var(--damask-blue) 140%);
  }
  .card--front .damask { left: 0; top: 0; width: 100%; height: 146px; }
  .card--front .trim {
    position: absolute; left: 0; top: 146px; width: 100%; height: 4px;
    background: var(--trim-tan);
  }
  .card--back .damask { left: 390px; top: 0; width: 240px; height: 100%; }
  .card--back .trim {
    position: absolute; left: 386px; top: 0; width: 4px; height: 100%;
    background: var(--trim-tan);
  }

  .label {
    position: absolute;
    background: linear-gradient(135deg, var(--parchment), var(--parchment-shade));
    border: 7px solid var(--frame-stone);
    outline: 2px solid var(--frame-dark);
    outline-offset: -11px;
    box-shadow: 0 4px 10px rgba(0,0,0,0.35);
  }
  .label--logo {
    left: 228px; top: 82px; width: 174px; height: 132px;
    display: flex; flex-direction: column; justify-content: center; align-items: center;
  }
  .wordmark {
    font-family: "Open Sans", sans-serif;
    font-weight: 600;
    color: var(--ink);
    line-height: 1.05;
    text-align: center;
  }
  .wordmark__name { font-size: 36px; letter-spacing: -1px; }
  .wordmark__trade { font-size: 24px; letter-spacing: -0.5px; }

  .label--contact {
    left: 160px; top: 60px; width: 440px; height: 240px;
    padding: 48px 54px 0 0;
    text-align: right;
    color: var(--ink);
  }
  .contact__name {
    font-family: "Cutive Mono", monospace;
    font-size: 28px;
    letter-spacing: 3px;
    margin-bottom: 10px;
  }
  .contact__line { font-size: 17px; line-height: 1.3; }
  .contact__links { font-size: 17px; margin-top: 4px; }
</style>
</head>
<body>
  <section class="card card--front" aria-label="Business card front">
    <div class="damask" role="img" aria-label="Olive and navy damask pattern band"></div>
    <div class="trim"></div>
    <div class="label label--logo">
      <div class="wordmark">
        <div class="wordmark__name">Tova</div>
        <div class="wordmark__trade">Interiors</div>
      </div>
    </div>
  </section>

  <section class="card card--back" aria-label="Business card back">
    <div class="damask" role="img" aria-label="Olive and navy damask pattern panel"></div>
    <div class="trim"></div>
    <div class="label label--contact">
      <p class="contact__name">Mira Hollen</p>
      <p class="contact__line">58 Wren Lane</p>
      <p class="contact__line">London</p>
      <p class="contact__links">mira@tova.com | +44 2071 48390</p>
      <p class="contact__line">www.tova.com</p>
    </div>
  </section>
</body>
</html>
```